Tarrow Creek plumbing plumbing company business card design

Something sinilar to business card i upload it is my old business card design
And have a good watermark with the logo or majority of the logot in rhe background as watermark

Plumbing business similar to uploaded design with a nice watermark of the logo

Font styles to use
Script

Colors

Designer to choose colors to be used in the design.

```html
<!DOCTYPE html>
<html lang="en">
<head>
<meta charset="utf-8">
<title>Tarrow Creek Plumbing — Business Card</title>
<link href="https://fonts.googleapis.com/css2?family=Roboto:wght@400;500;700&family=Dancing+Script:wght@700&display=swap" rel="stylesheet">
<style>
  :root {
    --backdrop: #1b1b1b;
    --card-front: #ffffff;
    --card-back: #000000;
    --brand-blue: #0a7cc4;
    --ink: #111111;
    --muted: #555555;
    --white: #ffffff;
  }
  * { margin: 0; padding: 0; box-sizing: border-box; }
  html, body {
    width: 1125px; height: 1200px; overflow: hidden;
    background: var(--backdrop);
    font-family: "Roboto", Arial, sans-serif;
  }
  .canvas { position: relative; width: 1125px; height: 1200px; }
  .card {
    position: absolute; left: 171px; width: 826px; height: 471px; overflow: hidden;
  }
  .card--front { top: 106px; background: var(--card-front); }
  .card--back { top: 640px; background: var(--card-back); }

  .brand {
    position: absolute; left: 112px; top: 196px;
    display: flex; align-items: center; gap: 12px;
  }
  .brand__square { width: 22px; height: 22px; background: var(--brand-blue); flex: none; }
  .brand__name {
    font-weight: 700; font-size: 27px; color: var(--ink); letter-spacing: 0.5px; white-space: nowrap;
  }

  .person { position: absolute; left: 473px; top: 86px; }
  .person__name {
    font-family: "Dancing Script", "Brush Script MT", cursive;
    font-size: 36px; font-weight: 700; color: var(--brand-blue); line-height: 1.05;
  }
  .person__title { font-size: 20px; font-weight: 500; color: var(--ink); line-height: 1.25; }

  .address {
    position: absolute; left: 473px; top: 166px;
    font-size: 19px; color: var(--muted); line-height: 25px; font-style: normal;
  }
  .contacts { position: absolute; left: 473px; top: 230px; list-style: none; }
  .contacts li {
    display: flex; align-items: center; gap: 12px;
    font-size: 19px; color: var(--muted); height: 26px; white-space: nowrap;
  }
  .contacts svg { width: 18px; height: 18px; fill: var(--brand-blue); flex: none; }

  .web-band {
    position: absolute; left: 0; top: 406px; width: 700px; height: 25px;
    background: var(--brand-blue);
  }
  .web-band__end {
    position: absolute; left: 690px; top: 400px; width: 24px; height: 37px;
    background: var(--brand-blue);
  }
  .web-band__url {
    position: absolute; left: 0; width: 800px; top: 406px; line-height: 25px;
    text-align: center; color: var(--white); font-size: 19px; letter-spacing: 4.6px;
  }

  .watermark {
    position: absolute; left: 0; top: 150px; width: 826px;
    display: flex; align-items: center; justify-content: center; gap: 22px;
    opacity: 0.12;
  }
  .watermark__square { width: 46px; height: 46px; background: var(--brand-blue); flex: none; }
  .watermark__name {
    font-weight: 700; font-size: 58px; color: var(--brand-blue); white-space: nowrap;
  }

  .back-url {
    position: absolute; left: 0; width: 704px; top: 391px;
    text-align: center; font-size: 19px; letter-spacing: 4.6px; color: var(--white);
  }
  .back-url__accent { color: var(--brand-blue); }
  .back-band {
    position: absolute; right: 0; top: 375px; width: 56px; height: 17px;
    background: var(--brand-blue);
  }
  .back-band__end {
    position: absolute; right: 56px; top: 367px; width: 22px; height: 33px;
    background: var(--brand-blue);
  }
</style>
</head>
<body>
<main class="canvas">
  <section class="card card--front">
    <div class="brand">
      <span class="brand__square"></span>
      <span class="brand__name">Tarrow Creek Plumbing</span>
    </div>

    <div class="person">
      <p class="person__name">Daniel Hart</p>
      <p class="person__title">President</p>
    </div>

    <address class="address">412 Willow Bend Road<br>Riverton, Oregon 97120</address>

    <ul class="contacts">
      <li><svg viewBox="0 0 24 24"><path d="M6.6 10.8a15.1 15.1 0 0 0 6.6 6.6l2.2-2.2c.3-.3.7-.4 1-.2 1.1.4 2.3.6 3.6.6.6 0 1 .4 1 1V20c0 .6-.4 1-1 1A17 17 0 0 1 3 4c0-.6.4-1 1-1h3.5c.6 0 1 .4 1 1 0 1.3.2 2.5.6 3.6.1.3 0 .7-.2 1z"/></svg>555-240-1187</li>
      <li><svg viewBox="0 0 24 24"><path d="M7 1h10a2 2 0 0 1 2 2v18a2 2 0 0 1-2 2H7a2 2 0 0 1-2-2V3a2 2 0 0 1 2-2zm0 3v14h10V4zm5 15.5a1 1 0 1 0 0 2 1 1 0 0 0 0-2z"/></svg>555-613-9042</li>
      <li><svg viewBox="0 0 24 24"><path d="M6 2h12v6H6zM3 9h18a1 1 0 0 1 1 1v8h-4v4H6v-4H2v-8a1 1 0 0 1 1-1zm5 7v4h8v-4z"/></svg>555-328-7716</li>
      <li><svg viewBox="0 0 24 24"><path d="M2 5h20v14H2zm2 2v.5l8 5 8-5V7zm0 2.8V17h16V9.8l-8 5z"/></svg>hello@tarrowcreek.com</li>
    </ul>

    <div class="web-band"></div>
    <div class="web-band__end"></div>
    <p class="web-band__url">www.tarrowcreekplumbing.com</p>
  </section>

  <section class="card card--back">
    <div class="watermark" aria-hidden="true">
      <span class="watermark__square"></span>
      <span class="watermark__name">Tarrow Creek Plumbing</span>
    </div>
    <p class="back-url">www.<span class="back-url__accent">tarrowcreekplumbing</span>.com</p>
    <div class="back-band__end"></div>
    <div class="back-band"></div>
  </section>
</main>
</body>
</html>
```